Web Design Pell Harbor

• An Overview of Pell Harbor for reference: We use to be a component manufacturing company. We sold to customers in USA and manage the builds in China using many manufacturing partners. We had a web site that served this market but we have transitioned over the last several years into “A unique design, development and program management company” It is this message we want to put up on the web now. We provide the design support, we help develop and test a new product for our customers and we provide the manufactured produce once we have transitioned it into production.
• The Target Market: Our customers are all high tech. Each product we produce is custom designed and sold only to one a specific customer. We work with a limited number of customer and sell to new customers by word of mouth and referrals. The web site is to provide a back ground check of any new referral so they can see who we are and our basic capabilities. It is not designed to sell customers or to find new customers but provide a background check to new potential customers.
• Pages Required: We estimate 12:
o Home/Title page is page 1 of PDF. It would have buttons to select other pages
o Names of other pages would be (short titles below if on button, if pull down menu the full title of slide)
 USA Facilities
 China Facilities
 Enclosures
 Antennas
 Connectors
 Cables
 EMI Shields
 Overlays
 Process Development
 VeraLink
 Contact Us (???) >> new page which we are not sure if we should or should not add.
• Design Specifics; attached is our logo, a PDF and PowerPoint slides showing the views we desire. We like these layouts, but perhaps a better one may be suggested for some artistic reason or layout. It should be clean, simple and user intuitive. We like the off white background and use for most of our presentations. One should be able to go from any screen to any other screen. The quote must include both design and implementation onto our web site which is http://pellharborsystems.example/
• Design Process:
We would like to see concepts of the Landing/Homepage, and an internal page initially. Feedback will be provided and you will be asked to continue if your layout is on the correct track.

• Implementation: Desire designer/implimentor to set up on their server. Allow us to test and edit on their site. We will provide password for implementation on our site after final approval.

Target Market(s)

• The Target Market: see above task descripiton

Industry/Entity Type

It Company

Requirements
Must have
• • Pages Required: We estimate 12:
 USA Facilities
 China Facilities
 Enclosures
 Antennas
 Connectors
 Cables
 EMI Shields
 Overlays
 Process Development
 VeraLink

Must have the implementation phase include in quote. see task description above
Should not have
• Should not be complex or long time loading.
Do not want any twitter or promotional add on functions.

```html
<!DOCTYPE html>
<html lang="en">
<head>
<meta charset="utf-8">
<title>Pell Harbor Technologies</title>
<link href="https://fonts.googleapis.com/css2?family=Montserrat:wght@400;600;700&family=Oswald:wght@600;700&display=swap" rel="stylesheet">
<style>
:root{
  --navy:#32376b;
  --blue:#0b70b9;
  --link:#0a68b0;
  --grey:#777a80;
  --map:#ececec;
  --pin:#d8321f;
  --pin-dark:#8a1a10;
  --white:#ffffff;
}
*{margin:0;padding:0;box-sizing:border-box}
html,body{width:1200px;height:885px;overflow:hidden;background:var(--white)}
body{position:relative;font-family:"Montserrat",Arial,sans-serif;color:var(--grey)}
a{text-decoration:none;color:inherit}
.abs{position:absolute}

.call{left:160px;top:47px;display:flex;align-items:center;gap:10px;font-size:11.5px}
.call-label{color:var(--grey)}
.call-number{color:var(--blue);font-weight:600;font-size:17px;margin-left:3px}

.nav-bar{top:84px;height:56px;background:var(--navy);display:flex;align-items:center;box-shadow:0 14px 14px -10px rgba(0,0,0,.35)}
.nav-left{left:160px;width:337px;padding-left:20px}
.nav-right{left:668px;width:372px;padding-left:25px}
.nav-bar a{color:var(--white);font-weight:700;font-size:10.5px;letter-spacing:-.2px;padding-right:15px;margin-right:15px;border-right:1px dotted rgba(255,255,255,.45);line-height:16px;white-space:nowrap}
.nav-bar a:last-child{border-right:0;margin-right:0}

.top-links{left:692px;top:58px;font-size:9.5px;font-weight:600;color:var(--link);display:flex;gap:8px}
.top-links span{color:var(--link)}

.brand{left:515px;top:37px;width:136px;height:137px;display:flex;flex-direction:column;align-items:center;justify-content:center;gap:10px}
.brand-mark{width:44px;height:44px;background:var(--blue)}
.brand-name{font-weight:700;font-size:19px;color:var(--blue);text-align:center;line-height:22px}
.brand-shadow{left:520px;top:196px;width:140px;height:10px;border-radius:50%;background:radial-gradient(ellipse at center,rgba(0,0,0,.18),rgba(0,0,0,0) 70%)}

.world-map{left:195px;top:178px;width:810px;height:385px;border-radius:45%;background:radial-gradient(ellipse at center,var(--map) 0%,#f2f2f2 55%,rgba(255,255,255,0) 75%)}

.location{font-size:8.6px;font-weight:600;color:var(--link);line-height:11.5px}
.loc-usa{left:325px;top:297px}
.loc-china{left:810px;top:257px}
.pin{width:42px;height:60px}
.pin-usa{left:284px;top:322px}
.pin-china{left:848px;top:281px}

.headline{left:248px;top:505px}
.headline text{font-family:"Oswald",Impact,sans-serif;font-weight:700}

.info-band{left:0;top:625px;width:1200px;height:184px;background:var(--blue);color:var(--white)}
.column{top:33px}
.col-who{left:181px;width:250px}
.col-products{left:479px;width:250px}
.col-signup{left:779px;width:240px}
.column h2{font-size:19px;font-weight:700;letter-spacing:-.6px;margin-bottom:15px;padding-left:2px}
.column p,.product-list li{font-size:10.6px;line-height:13.6px}
.product-list{list-style:none}
.product-list li{margin-bottom:5.6px}
.divider{top:33px;width:0;height:130px;border-left:1px dotted rgba(255,255,255,.5)}
.div-1{left:453px}
.div-2{left:747px}
.btn{position:absolute;height:21px;border-radius:4px;background:var(--navy);color:var(--white);font-size:10.5px;font-weight:700;display:flex;align-items:center;justify-content:center;letter-spacing:-.3px}
.btn-read{left:180px;top:133px;width:80px}
.btn-more{left:480px;top:133px;width:102px}
.btn-login{left:781px;top:133px;width:80px}
.field{position:absolute;left:780px;width:236px;height:28px;background:var(--white);border-radius:6px;display:flex;align-items:center;color:var(--grey);font-size:11px;box-shadow:inset 0 0 0 1px #dcdcdc}
.field-email{top:66px}
.field-pass{top:99px}
.field-icon{width:42px;display:flex;justify-content:center;border-right:1px dotted #bbb;height:16px;align-items:center}
.field span{padding-left:12px}

.footer-links{left:180px;top:828px;font-size:10.4px;color:var(--grey)}
.copyright{left:180px;top:852px;font-size:9px;font-weight:700;color:#909090}
.copyright a{color:var(--link);margin-left:3px}
</style>
</head>
<body>

<div class="abs call">
  <svg width="28" height="28" viewBox="0 0 28 28" aria-hidden="true"><circle cx="14" cy="14" r="12.5" fill="none" stroke="var(--navy)" stroke-width="1.5"/><path d="M11 8c-1.5 1-2 2.5-1.3 5 .8 3 2.6 5.3 4.6 6.4 1.6.8 2.7.4 3.3-.4l-2-2.2-1.5.8c-1-.7-2-2.3-2.4-3.8l1.3-1L11.7 8z" fill="var(--navy)"/></svg>
  <span class="call-label">Call Us TODAY:</span><span class="call-number">0800 2040 3060</span>
</div>

<nav class="abs nav-bar nav-left">
  <a href="#">USA FACILITIES</a><a href="#">CHINA FACILITIES</a><a href="#">ENCLOSURES</a>
</nav>

<div class="abs brand">
  <div class="brand-mark"></div>
  <div class="brand-name">PELL HARBOR</div>
</div>
<div class="abs brand-shadow"></div>

<div class="abs top-links">
  <a href="#">OVERLAYS</a><span>|</span><a href="#">PROCESS DEVELOPMENT</a><span>|</span><a href="#">VERALINK</a><span>|</span><a href="#">CONTACT US</a>
</div>

<nav class="abs nav-bar nav-right">
  <a href="#">ANTENNAS</a><a href="#">CONNECTORS</a><a href="#">CABLES</a><a href="#">EMI SHIELDS</a>
</nav>

<div class="abs world-map" role="img" aria-label="Faint grey world map showing the continents"></div>

<p class="abs location loc-usa">48 Tidewater Road<br>Suite 210 Marlow Bay, CA<br>95190</p>
<svg class="abs pin pin-usa" viewBox="0 0 42 60" aria-hidden="true"><ellipse cx="21" cy="55" rx="8" ry="2" fill="rgba(0,0,0,.15)"/><path d="M21 2C10 2 2 10 2 20c0 12 19 31 19 31s19-19 19-31C40 10 32 2 21 2z" fill="var(--pin)"/><circle cx="21" cy="20" r="7" fill="var(--pin-dark)"/></svg>

<p class="abs location loc-china">Lanshan Tech District<br>Qiaoyuan Lu #17 Lanshan, China<br>100288</p>
<svg class="abs pin pin-china" viewBox="0 0 42 60" aria-hidden="true"><ellipse cx="21" cy="55" rx="8" ry="2" fill="rgba(0,0,0,.15)"/><path d="M21 2C10 2 2 10 2 20c0 12 19 31 19 31s19-19 19-31C40 10 32 2 21 2z" fill="var(--pin)"/><circle cx="21" cy="20" r="7" fill="var(--pin-dark)"/></svg>

<svg class="abs headline" width="660" height="95" viewBox="0 0 660 95">
  <text x="2" y="43" font-size="50" fill="var(--blue)" textLength="654" lengthAdjust="spacingAndGlyphs">A UNIQUE DESIGN, DEVELOPMENT AND</text>
  <text x="2" y="91" font-size="58" fill="var(--navy)" textLength="650" lengthAdjust="spacingAndGlyphs">PROGRAM MANAGEMENT COMPANY</text>
</svg>

<section class="abs info-band">
  <div class="abs column col-who">
    <h2>WHO WE ARE?</h2>
    <p>Lorem ipsum dolor sit amet, consectetuer adipiscing elit, sed diam nonummy nibh euismod tincidunt ut laoreet dolore magna aliquam erat volutpat.</p>
  </div>
  <a class="btn btn-read" href="#">Read More...</a>

  <div class="abs divider div-1"></div>

  <div class="abs column col-products">
    <h2>OUR PRODUCTS</h2>
    <ul class="product-list">
      <li>Custom Enclosure Design and Development</li>
      <li>Custom Antenna Design and Development</li>
      <li>Custom Connector Design and Development</li>
    </ul>
  </div>
  <a class="btn btn-more" href="#">More Products...</a>

  <div class="abs divider div-2"></div>

  <div class="abs column col-signup">
    <h2>SIGN UP WITH US</h2>
  </div>
  <div class="field field-email">
    <div class="field-icon"><svg width="16" height="12" viewBox="0 0 16 12" aria-hidden="true"><rect x="1" y="1" width="14" height="10" fill="none" stroke="#333" stroke-width="1.4"/><path d="M1 1l7 6 7-6" fill="none" stroke="#333" stroke-width="1.4"/></svg></div>
    <span>Enter Your Email Address</span>
  </div>
  <div class="field field-pass">
    <div class="field-icon"><svg width="16" height="16" viewBox="0 0 16 16" aria-hidden="true"><circle cx="11" cy="5" r="3.5" fill="#333"/><path d="M9 7L2 14M4 12l2 2M3 13l1.5 1.5" stroke="#333" stroke-width="1.8" fill="none"/></svg></div>
    <span>Enter Your Password</span>
  </div>
  <a class="btn btn-login" href="#">Login</a>
</section>

<footer>
  <p class="abs footer-links">USA Facilities - China Facilities - Enclosures - Antennas - Connectors - Cables - EMI Shields - Overlays - Process Development - VeraLink -&nbsp; Contact Us</p>
  <p class="abs copyright">PELL HARBOR TECHNOLOGIES © 2013 - <a href="#">Privacy Policy</a></p>
</footer>

</body>
</html>
```